Redesign of an insurance website

Attached is an insurance website that I need to redesign. Currently the website is too dark. I like for example www.brenvalo.com . Could you make the website lighter and change the structure a little so that it is more user friendly?

Industry/Entity Type

Insurance

Number of Pages Required

4 page

```html
<!DOCTYPE html>
<html lang="en">
<head>
<meta charset="utf-8">
<title>Saferio.cz – Insuring Your Trust</title>
<link rel="stylesheet" href="https://fonts.googleapis.com/css2?family=Montserrat:wght@400;600;700;800&family=Open+Sans:wght@400;600;700&display=swap">
<style>
:root{
  --blue:#1f7fe3;
  --orange:#f7941d;
  --ink:#2b2b2b;
  --muted:#9a9a9a;
  --line:#dcdcdc;
  --soft:#f3f3f3;
  --footer:#1f2230;
  --footer-band:#282b3a;
  --white:#ffffff;
}
*{box-sizing:border-box;margin:0;padding:0}
html,body{width:1200px;height:3186px;overflow:hidden;background:var(--white)}
body{font-family:"Open Sans",Arial,sans-serif;color:var(--ink);position:relative}
h1,h2,h3,h4,.brand,.btn{font-family:"Montserrat",Arial,sans-serif}
section,header,footer{position:absolute;left:0;width:1200px}
.btn{position:absolute;display:flex;align-items:center;justify-content:center;border-radius:20px;font-size:11px;font-weight:700;letter-spacing:.3px;text-transform:uppercase}
.btn-blue{background:var(--blue);color:var(--white)}
.btn-white{background:var(--white);color:var(--ink)}
.btn-orange{background:var(--orange);color:var(--white)}
.photo{position:absolute}
.sec-title{position:absolute;left:0;width:1200px;text-align:center;color:var(--blue);font-weight:700;font-size:31px;letter-spacing:.3px}
.sec-sub{position:absolute;left:0;width:1200px;text-align:center;font-family:"Montserrat",Arial,sans-serif;font-weight:600;font-size:17px;color:#333}
.sec-lead{position:absolute;left:360px;width:480px;text-align:center;font-size:11.5px;line-height:19px;color:#888}
.dots{position:absolute;left:0;width:1200px;display:flex;justify-content:center;gap:6px}
.dots span{width:9px;height:9px;border-radius:50%;background:#cfcfcf}
.dots span.on{background:var(--blue)}

/* header */
.site-header{top:0;height:65px;background:var(--white)}
.brand{position:absolute;font-weight:800;font-size:22px;color:var(--blue);letter-spacing:.2px}
.nav a{position:absolute;top:25px;font-size:12px;color:#444;text-decoration:none}
.nav .login{font-weight:700;font-family:"Montserrat",Arial,sans-serif;font-size:11px;top:26px}

/* hero */
.hero{top:65px;height:508px;background:linear-gradient(90deg,#14161b 0%,#2b2f36 40%,#5a5f66 70%,#8a8e92 100%)}
.hero h1{position:absolute;left:249px;top:140px;color:var(--white);font-size:44px;line-height:50px;font-weight:800}
.hero p{position:absolute;left:249px;top:252px;width:320px;color:#e4e4e4;font-size:10.5px;line-height:18px}

/* quote */
.quote{top:573px;height:235px;background:#f6f6f6}
.quote-icon{position:absolute;left:262px;top:112px}
.field{position:absolute;width:182px;height:32px;border:1px solid var(--line);background:var(--white);font-size:10px;color:#999;padding:0 10px;display:flex;align-items:center}
.calc{position:absolute;left:768px;top:165px;width:182px;height:33px;background:var(--blue);color:var(--white);font-family:"Montserrat",Arial,sans-serif;font-weight:700;font-size:11px;display:flex;align-items:center;justify-content:center}

/* types */
.types{top:808px;height:274px;background:var(--white)}
.pointer{position:absolute;left:302px;top:0;width:0;height:0;border-left:16px solid transparent;border-right:16px solid transparent;border-top:16px solid #f6f6f6}
.type{position:absolute;top:42px;width:170px;text-align:center}
.type .ring{width:76px;height:76px;margin:0 auto;border-radius:50%;border:2px solid #dedede;display:flex;align-items:center;justify-content:center;background:var(--white)}
.type.active .ring{border-color:var(--blue)}
.type h4{margin-top:14px;font-size:11px;font-weight:600;color:#666;letter-spacing:.2px}
.type.active h4{color:var(--blue)}
.type p{margin-top:6px;font-size:9.5px;line-height:14px;color:var(--muted)}

/* split */
.split{top:1082px;height:318px;background:var(--white)}
.split h2{position:absolute;left:630px;top:28px;font-size:20px;line-height:26px;font-weight:700;color:var(--blue)}
.split h2 span{display:block;color:#333;font-weight:400}
.split-copy{position:absolute;left:630px;top:92px;width:326px;display:flex;flex-direction:column;gap:14px}
.split-copy p{font-size:9.5px;line-height:16px;color:#777}

/* services */
.services{top:1400px;height:443px;background:var(--white)}
.svc{position:absolute;top:118px;width:222px}
.svc .photo{position:relative;width:222px;height:200px;border:4px solid #e9e9e9}
.svc h3{margin-top:16px;font-size:13px;font-weight:700;color:#222}
.svc p{margin-top:6px;font-size:10.5px;line-height:16px;color:var(--muted)}

/* testimonials */
.clients{top:1843px;height:412px;background:var(--soft)}
.client{position:absolute;top:150px;width:240px;text-align:center}
.client .avatar{width:80px;height:80px;margin:0 auto;border-radius:50%;border:4px solid var(--white);background:linear-gradient(160deg,#c9cdd3,#4a4f57);box-shadow:0 1px 3px rgba(0,0,0,.15)}
.client h4{margin-top:12px;font-size:14px;font-weight:600;color:#222}
.stars{margin-top:4px;color:var(--orange);font-size:13px;letter-spacing:1px}
.client p{margin:6px auto 0;width:190px;font-size:10px;line-height:15px;color:#777}

/* blog */
.blog{top:2255px;height:540px;background:var(--white)}
.post{position:absolute;top:150px;width:222px;height:348px;background:var(--white);box-shadow:0 1px 4px rgba(0,0,0,.18)}
.post .photo{position:relative;width:222px;height:172px}
.post .date{margin:16px 16px 0;font-family:"Montserrat",Arial,sans-serif;font-size:9.5px;font-weight:700;color:var(--blue)}
.post h3{margin:10px 16px 0;font-size:12px;line-height:16px;font-weight:700;color:#222}
.post p{margin:10px 16px 0;font-size:10px;line-height:15px;color:#888}
.post .meta{position:absolute;left:0;bottom:0;width:222px;height:30px;border-top:1px solid #e6e6e6;display:flex;align-items:center;justify-content:space-between;padding:0 16px;font-size:9px;color:#666}
.post .meta b{font-family:"Montserrat",Arial,sans-serif;color:var(--blue);font-size:10px}

/* footer */
.site-footer{top:2795px;height:391px;background:var(--footer);color:#c9cbd3}
.contact-band{position:absolute;left:249px;top:0;width:703px;height:93px;background:var(--footer-band)}
.contact{position:absolute;top:24px;width:230px;height:46px}
.contact .ico{position:absolute;left:0;top:4px;width:38px;height:38px;background:#1d202c;display:flex;align-items:center;justify-content:center}
.contact h4{position:absolute;left:56px;top:0;color:var(--white);font-size:11.5px;font-weight:600;white-space:nowrap}
.contact p{position:absolute;left:56px;top:16px;width:170px;font-size:9px;line-height:14px;color:#d5d7de}
.fcol{position:absolute;top:132px}
.fcol h4{color:var(--white);font-size:12.5px;font-weight:700;letter-spacing:.3px}
.fcol h4::after{content:"";display:block;width:46px;height:2px;background:var(--blue);margin-top:7px}
.fcol p{font-size:9.5px;line-height:15px;color:#8d909c}
.links{list-style:none;font-size:9px;line-height:18.5px;color:#8d909c}
.links li::before{content:"›";margin-right:7px;color:#8d909c}
.newsletter input{width:170px;height:26px;border:1px solid #3a3d4c;background:#262938;color:#888;font-size:9px;padding:0 8px;font-family:"Open Sans",Arial,sans-serif}
.social{display:flex;gap:4px}
.social span{width:18px;height:18px;border-radius:50%;background:#4d6fbf}
.bottom-line{position:absolute;left:249px;top:345px;width:703px;height:1px;background:#33364a}
.copyright{position:absolute;left:249px;top:361px;font-size:9.5px;color:#d5d7de}
</style>
</head>
<body>

<header class="site-header">
  <div class="brand" style="left:249px;top:19px">SAFERIO.CZ</div>
  <nav class="nav">
    <a style="left:597px">Insurance</a>
    <a style="left:672px">Information</a>
    <a class="login" style="left:768px">LOG IN</a>
  </nav>
  <div class="btn btn-orange" style="left:825px;top:15px;width:127px;height:36px">Register</div>
</header>

<section class="hero">
  <div class="photo" role="img" aria-label="Photo of two businessmen in suits reviewing a document together in a bright office" style="left:520px;top:0;width:680px;height:508px;background:linear-gradient(100deg,rgba(30,33,40,0) 0%,rgba(120,125,132,.35) 60%,rgba(200,203,206,.25) 100%)"></div>
  <h1>INSURING<br>YOUR TRUST</h1>
  <p>Lorem Ipsum is simply dummy text of the printing and typesetting industry. Lorem Ipsum has been the industry's standard dummy text ever since the 1500s.</p>
  <div class="btn btn-blue" style="left:249px;top:320px;width:127px;height:34px">Read More</div>
  <div class="btn btn-white" style="left:400px;top:320px;width:127px;height:34px">Start Quote</div>
</section>

<section class="quote">
  <h2 class="sec-title" style="top:30px">YOU CAN FIND MOST</h2>
  <div class="sec-sub" style="top:70px">ADVANTAGEOUS INSURANCE</div>
  <svg class="quote-icon" width="92" height="80" viewBox="0 0 92 80" aria-hidden="true">
    <path d="M10 8h34v64H10z" fill="none" stroke="#1f7fe3" stroke-width="7"/>
    <path d="M26 20h12v40H26z" fill="#1f7fe3"/>
    <path d="M44 30l14 6v24l-14 6z" fill="#1f7fe3"/>
    <path d="M64 48l10 -6M66 58l12 0M64 68l10 6" stroke="#1f7fe3" stroke-width="4" stroke-linecap="round"/>
  </svg>
  <div class="field" style="left:370px;top:113px">First Name</div>
  <div class="field" style="left:568px;top:113px">Last Name</div>
  <div class="field" style="left:768px;top:113px">Email ID</div>
  <div class="field" style="left:370px;top:165px">Phone Number</div>
  <div class="field" style="left:568px;top:165px">Zip Code</div>
  <div class="calc">CALCULATE PRICE</div>
</section>

<section class="types">
  <div class="pointer"></div>
  <div class="type active" style="left:233px">
    <div class="ring"><svg width="36" height="36" viewBox="0 0 36 36" aria-hidden="true"><rect x="6" y="5" width="14" height="26" fill="none" stroke="#1f7fe3" stroke-width="3"/><rect x="12" y="11" width="5" height="14" fill="#1f7fe3"/><path d="M24 22l6 4M24 28h7" stroke="#1f7fe3" stroke-width="2"/></svg></div>
    <h4>ACCIDENT INSURANCE</h4>
    <p>Lorem Ipsum is simply dummy text of the printing and typesetting industry. Lorem Ipsum has been the industry's</p>
  </div>
  <div class="type" style="left:415px">
    <div class="ring"><svg width="34" height="34" viewBox="0 0 24 24" aria-hidden="true"><path d="M21 16v-2l-8-5V3.5a1.5 1.5 0 0 0-3 0V9l-8 5v2l8-2.5V19l-2 1.5V22l3.5-1 3.5 1v-1.5L13 19v-5.5z" fill="#c4c4c4"/></svg></div>
    <h4>TRAVEL INSURANCE</h4>
    <p>Lorem Ipsum is simply dummy text of the printing and typesetting industry. Lorem Ipsum has been the industry's</p>
  </div>
  <div class="type" style="left:601px">
    <div class="ring"><svg width="34" height="34" viewBox="0 0 24 24" aria-hidden="true"><circle cx="10" cy="7" r="4" fill="#c4c4c4"/><path d="M2 21c0-5 4-8 8-8s8 3 8 8z" fill="#c4c4c4"/><circle cx="18" cy="17" r="4" fill="#fff" stroke="#c4c4c4" stroke-width="2"/></svg></div>
    <h4>BUSINESS INSURANCE</h4>
    <p>Lorem Ipsum is simply dummy text of the printing and typesetting industry. Lorem Ipsum has been the industry's</p>
  </div>
  <div class="type" style="left:781px">
    <div class="ring"><svg width="34" height="34" viewBox="0 0 24 24" aria-hidden="true"><path d="M12 3L2 12h3v9h5v-6h4v6h5v-9h3z" fill="#c4c4c4"/></svg></div>
    <h4>HOME INSURANCE</h4>
    <p>Lorem Ipsum is simply dummy text of the printing and typesetting industry. Lorem Ipsum has been the industry's</p>
  </div>
  <div class="dots" style="top:227px"><span class="on"></span><span></span><span></span><span></span></div>
</section>

<section class="split">
  <div class="photo" role="img" aria-label="Photo of colleagues around an office table reviewing insurance paperwork" style="left:0;top:0;width:600px;height:318px;background:linear-gradient(120deg,#e8e6e3 0%,#b9b6b2 45%,#6a7080 75%,#d7d2cb 100%)"></div>
  <h2>YOU CLOSED THE PREVIOUSLY<span>DISADVANTAGE INSURANCE</span></h2>
  <div class="split-copy">
    <p>Lorem Ipsum is simply dummy text of the printing and typesetting industry. Lorem Ipsum has been the industry's standard dummy text ever since the 1500s, when an unknown printer took a galley of type and scrambled it to make a type specimen book.</p>
    <p>Lorem Ipsum is simply dummy text of the printing and typesetting industry. Lorem Ipsum has been the industry's standard dummy text ever since the 1500s, when an unknown printer took a galley of type and scrambled it to make a type specimen book.</p>
  </div>
  <div class="btn btn-blue" style="left:630px;top:252px;width:127px;height:34px">Read More</div>
</section>

<section class="services">
  <h2 class="sec-title" style="top:38px">BEST SERVICE</h2>
  <div class="sec-sub" style="top:72px;font-size:15px">INSURANCE COVERAGE</div>
  <div class="svc" style="left:249px">
    <div class="photo" role="img" aria-label="Photo of a family standing beside a red car" style="background:linear-gradient(135deg,#d9c9c0,#b0322f 60%,#8c8c8c)"></div>
    <h3>AUTO INSURANCE</h3>
    <p>Lorem Ipsum is simply dummy text of the printing and typesetting industry. Lorem Ipsum has been the industry's</p>
  </div>
  <div class="svc" style="left:488px">
    <div class="photo" role="img" aria-label="Photo of a couple looking at a laptop with an advisor" style="background:linear-gradient(135deg,#cfc8bd,#8a7c6c 55%,#e2ddd4)"></div>
    <h3>GET LIFE INSURANCE</h3>
    <p>Lorem Ipsum is simply dummy text of the printing and typesetting industry. Lorem Ipsum has been the industry's</p>
  </div>
  <div class="svc" style="left:726px">
    <div class="photo" role="img" aria-label="Photo of a damaged motorbike lying on the road" style="background:linear-gradient(135deg,#9b9d9f,#3a3b3d 55%,#b6b3ae)"></div>
    <h3>BIKE INSURANCE</h3>
    <p>Lorem Ipsum is simply dummy text of the printing and typesetting industry. Lorem Ipsum has been the industry's</p>
  </div>
</section>

<section class="clients">
  <h2 class="sec-title" style="top:40px">WHAT OUR CLIENTS SAY'S</h2>
  <p class="sec-lead" style="top:84px">Lorem Ipsum is simply dummy text of the printing and typesetting industry. Lorem Ipsum has been the industry's standard dummy text ever since the 1500s.</p>
  <div class="client" style="left:229px">
    <div class="avatar" role="img" aria-label="Portrait of client Tomas Marek"></div>
    <h4>Tomas Marek</h4>
    <div class="stars">★★★★★</div>
    <p>Lorem Ipsum is simply dummy text of the printing and typesetting industry. Lorem Ipsum has been the industry's</p>
  </div>
  <div class="client" style="left:475px">
    <div class="avatar" role="img" aria-label="Portrait of client Eva Holub"></div>
    <h4>Eva Holub</h4>
    <div class="stars">★★★★★</div>
    <p>Lorem Ipsum is simply dummy text of the printing and typesetting industry. Lorem Ipsum has been the industry's</p>
  </div>
  <div class="client" style="left:719px">
    <div class="avatar" role="img" aria-label="Portrait of client Petr Lorenc"></div>
    <h4>Petr Lorenc</h4>
    <div class="stars">★★★★★</div>
    <p>Lorem Ipsum is simply dummy text of the printing and typesetting industry. Lorem Ipsum has been the industry's</p>
  </div>
  <div class="dots" style="top:370px"><span class="on"></span><span></span><span></span><span></span></div>
</section>

<section class="blog">
  <h2 class="sec-title" style="top:38px">RECENT FROM BLOG</h2>
  <p class="sec-lead" style="top:82px">Lorem Ipsum is simply dummy text of the printing and typesetting industry. Lorem Ipsum has been the industry's standard dummy text ever since the 1500s.</p>
  <article class="post" style="left:240px">
    <div class="photo" role="img" aria-label="Photo of an advisor explaining a contract to two clients" style="background:linear-gradient(135deg,#e4e1dc,#6d6660 55%,#bfb8ae)"></div>
    <div class="date">NOVEMBER - 20 , 2017</div>
    <h3>LIFE INSURANCE FOR THE STAGES OF YOUR LIFE</h3>
    <p>Lorem Ipsum is simply dummy text of the printing and typesetting industry. Lorem Ipsum has been the industry's</p>
    <div class="meta"><span>Posted by : Admin</span><b>READ MORE</b></div>
  </article>
  <article class="post" style="left:480px">
    <div class="photo" role="img" aria-label="Photo of a team meeting in a bright open office" style="background:linear-gradient(135deg,#dfe3e6,#5a5e63 55%,#a9adb1)"></div>
    <div class="date">NOVEMBER - 20 , 2017</div>
    <h3>MATCHING LIFE INSURANCE TO YOUR NEEDS</h3>
    <p>Lorem Ipsum is simply dummy text of the printing and typesetting industry. Lorem Ipsum has been the industry's</p>
    <div class="meta"><span>Posted by : Admin</span><b>READ MORE</b></div>
  </article>
  <article class="post" style="left:720px">
    <div class="photo" role="img" aria-label="Top-down photo of a desk with charts, laptops and papers" style="background:linear-gradient(135deg,#8a5a34,#c9a27a 50%,#5a3a22)"></div>
    <div class="date">NOVEMBER - 20 , 2017</div>
    <h3>UNDERSTANDING THE TYPES OF LIFE INSURANCE</h3>
    <p>Lorem Ipsum is simply dummy text of the printing and typesetting industry. Lorem Ipsum has been the industry's</p>
    <div class="meta"><span>Posted by : Admin</span><b>READ MORE</b></div>
  </article>
</section>

<footer class="site-footer">
  <div class="contact-band">
    <div class="contact" style="left:50px">
      <div class="ico"><svg width="14" height="18" viewBox="0 0 24 30" aria-hidden="true"><path d="M12 0C5.4 0 0 5.2 0 11.6 0 20 12 30 12 30s12-10 12-18.4C24 5.2 18.6 0 12 0zm0 16a4.5 4.5 0 1 1 0-9 4.5 4.5 0 0 1 0 9z" fill="#fff"/></svg></div>
      <h4>Address</h4>
      <p>Lorem Ipsum is simply dummy text of the printing and typesetting industry.</p>
    </div>
    <div class="contact" style="left:298px">
      <div class="ico"><svg width="20" height="14" viewBox="0 0 24 16" aria-hidden="true"><rect x="1" y="1" width="22" height="14" fill="none" stroke="#fff" stroke-width="2"/><path d="M1 1l11 8 11-8" fill="none" stroke="#fff" stroke-width="2"/></svg></div>
      <h4>Email</h4>
      <p>info@saferio.cz<br>info@saferio.cz</p>
    </div>
    <div class="contact" style="left:496px">
      <div class="ico"><svg width="18" height="18" viewBox="0 0 24 24" aria-hidden="true"><path d="M6.6 10.8a15 15 0 0 0 6.6 6.6l2.2-2.2a1 1 0 0 1 1-.25 11.4 11.4 0 0 0 3.6.57 1 1 0 0 1 1 1V20a1 1 0 0 1-1 1A17 17 0 0 1 3 4a1 1 0 0 1 1-1h3.5a1 1 0 0 1 1 1c0 1.25.2 2.45.57 3.57a1 1 0 0 1-.25 1z" fill="#fff"/></svg></div>
      <h4>Call Center</h4>
      <p style="width:150px"><b style="color:#fff">Mobile</b> : 000 0000 0000<br><b style="color:#fff">Fax</b> : 000 0000 0000</p>
    </div>
  </div>

  <div class="fcol" style="left:249px;width:240px">
    <div class="brand" style="position:static;color:#fff;font-size:21px">SAFERIO.CZ</div>
    <p style="margin-top:16px">Lorem Ipsum is simply dummy text of the printing and typesetting industry. Lorem Ipsum has been the industry's standard dummy text ever since the 1500s, when an unknown printer took a galley of type and scrambled it to make a type specimen book. It has survived not only five centuries, but also the leap into electronic typesetting.</p>
  </div>

  <div class="fcol" style="left:508px;width:210px">
    <h4>IMPORTANT LINK</h4>
    <div style="display:flex;gap:34px;margin-top:14px">
      <ul class="links">
        <li>Accident Insurance</li><li>Travel Insurance</li><li>Home Insurance</li><li>Business Insurance</li><li>Manager Insurance</li><li>Learn Insurance</li><li>Insurance Guides</li>
      </ul>
      <ul class="links">
        <li>Motorcycle</li><li>Auto</li><li>Boat</li><li>Life Insurance</li>
      </ul>
    </div>
  </div>

  <div class="fcol newsletter" style="left:735px;width:217px">
    <h4>NEWSLETTER</h4>
    <p style="margin-top:14px">Lorem Ipsum is simply dummy text of the printing and typesetting industry. Lorem Ipsum has been the industry's</p>
    <div style="display:flex;gap:8px;margin-top:12px;align-items:center">
      <input type="text" value="Your Email Address" readonly>
      <div style="width:30px;height:26px;background:var(--blue);display:flex;align-items:center;justify-content:center"><svg width="13" height="13" viewBox="0 0 24 24" aria-hidden="true"><path d="M2 21l21-9L2 3v7l15 2-15 2z" fill="#fff"/></svg></div>
    </div>
    <h4 style="margin-top:18px">STAY CONNECTED</h4>
    <div class="social" style="margin-top:12px"><span></span><span></span><span></span><span></span><span></span><span></span></div>
  </div>

  <div class="bottom-line"></div>
  <div class="copyright">Copyright © 2017 <b style="color:#fff">SAFERIO</b> . All Rights Reserved.</div>
</footer>

</body>
</html>
```